Business card design with slight adjustment to current logo
Marlow Heating Cooling & Plumbing
Business card design with slight adjustment to current logo - Trade
Creative Brief
Bright & Fun-filled
no name wanted on card
no title wanted on card
3167 Penwick Ave Findlay, OH 45893
marlowhvacfindlay@examplemail.test
marlow-hvac.test
Heating Cooling Plumbing The logo I have is an older logo, we want to keep it the same but the type of file I have it flat looking, plain colored. If the logo can be tweaked to look brighter, less flat, but very similar so as not to look much different I would appreciate that. My hope was to have the flame in the logo look a little more like a flame, I think maybe the curve of it is just a little off, making it more like a shark fin or something. for the logo and business card, that color blue in logo is a favorite.
Tkvorel42 Tkvorel42
Cards can also say: Service & Install Free Estimates
This is more me looking for business card designs, if the logo can be adjusted a little bit and you have the idea for it, fine. But mainly I need good business card designs for current logo

```html
<!DOCTYPE html>
<html lang="en">
<head>
<meta charset="utf-8">
<title>Marlow Heating Cooling &amp; Plumbing – Stationery</title>
<link href="https://fonts.googleapis.com/css2?family=Montserrat:wght@400;600;700;800&family=Open+Sans:wght@400;600&display=swap" rel="stylesheet">
<style>
  :root {
    --stage: #a4a4a4;
    --paper: #ffffff;
    --ink: #1b1b1b;
    --text: #555555;
    --muted: #8a8a8a;
    --brand-blue: #1f8fe0;
    --band-black: #161616;
    --rule: #d6d6d6;
  }
  * { box-sizing: border-box; margin: 0; padding: 0; }
  html, body { width: 1200px; height: 935px; overflow: hidden; }
  body {
    background: var(--stage);
    position: relative;
    font-family: "Open Sans", Arial, sans-serif;
    color: var(--text);
  }
  .sheet {
    position: absolute;
    background: var(--paper);
    box-shadow: 0 2px 5px rgba(0,0,0,.18);
    overflow: hidden;
  }

  /* Wordmark */
  .wordmark {
    position: absolute;
    font-family: "Montserrat", Arial, sans-serif;
    font-weight: 800;
    color: var(--ink);
    line-height: 1;
    display: flex;
    align-items: center;
    gap: .3em;
    white-space: nowrap;
  }
  .wordmark .dot {
    width: .55em; height: .55em;
    border-radius: 50%;
    background: var(--brand-blue);
    flex: none;
  }
  .wordmark .name { display: block; }
  .wordmark .name small {
    display: block;
    font-size: .28em;
    letter-spacing: .04em;
    margin-top: .25em;
    text-transform: uppercase;
  }

  /* Bottom band */
  .band { position: absolute; left: 0; right: 0; bottom: 0; }
  .band .black { position: absolute; left: 0; top: 0; bottom: 0; background: var(--band-black); }
  .band .blue  { position: absolute; right: 0; top: 0; bottom: 0; background: var(--brand-blue); }
  .band .badge {
    position: absolute; border-radius: 50%;
    background: var(--paper);
    display: flex; align-items: center; justify-content: center;
  }
  .band .badge span { border-radius: 50%; background: var(--brand-blue); display: block; }

  .contact {
    position: absolute;
    font-size: 6px;
    line-height: 1.55;
    color: var(--text);
    white-space: nowrap;
  }
  .contact .line { display: flex; align-items: center; gap: 3px; }
  .contact svg { width: 6px; height: 6px; flex: none; }

  /* Letterhead */
  .letterhead { left: 38px; top: 56px; width: 493px; height: 830px; }
  .letterhead .wordmark { left: 34px; top: 40px; font-size: 30px; }
  .letterhead .contact { right: 34px; top: 30px; font-size: 6.5px; }
  .letterhead .header-rule {
    position: absolute; left: 34px; right: 34px; top: 100px;
    height: 1px; background: var(--rule);
  }
  .letter-body {
    position: absolute; left: 34px; right: 50px; top: 265px;
    font-size: 7.4px; line-height: 1.5; color: var(--text);
  }
  .letter-body .salutation {
    font-family: "Montserrat", Arial, sans-serif;
    font-weight: 700; font-size: 11px; color: var(--ink);
    margin-bottom: 16px;
  }
  .letter-body p { margin-bottom: 11px; }
  .letter-body .closing { margin-top: 16px; font-size: 6px; font-weight: 600; color: var(--ink); }
  .signature {
    width: 70px; height: 22px; margin-top: 14px;
    background: linear-gradient(90deg, rgba(30,30,30,.55), rgba(30,30,30,.25));
    border-radius: 3px;
  }
  .letterhead .band { height: 36px; }
  .letterhead .band .black { top: 10px; height: 12px; right: 0; }
  .letterhead .band .blue { top: 10px; height: 12px; width: 95px; }
  .letterhead .band .badge { right: 36px; top: 0; width: 34px; height: 34px; }
  .letterhead .band .badge span { width: 24px; height: 24px; }

  /* Business card front */
  .card-front { left: 587px; top: 121px; width: 248px; height: 145px; }
  .card-front .wordmark { left: 14px; top: 48px; font-size: 17px; }
  .card-front .divider { position: absolute; left: 118px; top: 34px; width: 1px; height: 64px; background: var(--rule); }
  .card-front .contact { left: 126px; top: 32px; font-size: 5.2px; }
  .card-front .band { height: 24px; }
  .card-front .band .black { top: 8px; height: 8px; right: 0; }
  .card-front .band .blue { top: 8px; height: 8px; width: 44px; }
  .card-front .band .badge { right: 16px; top: 0; width: 22px; height: 22px; }
  .card-front .band .badge span { width: 15px; height: 15px; }

  /* Business card back */
  .card-back { left: 873px; top: 101px; width: 278px; height: 165px; background: var(--brand-blue); }
  .card-back .wordmark { left: 50%; top: 50%; transform: translate(-50%,-50%); font-size: 34px; color: rgba(255,255,255,.28); }
  .card-back .wordmark .dot { background: rgba(255,255,255,.28); }

  /* Envelope */
  .envelope { left: 587px; top: 304px; width: 564px; height: 227px; }
  .envelope .flap { position: absolute; inset: 0; }
  .envelope .wordmark { left: 50%; top: 48px; transform: translateX(-50%); font-size: 26px; }

  /* Compliment card */
  .compliment { left: 587px; top: 582px; width: 564px; height: 245px; }
  .compliment .wordmark { left: 22px; top: 36px; font-size: 24px; }
  .compliment .contact { left: 22px; top: 96px; font-size: 5.8px; }
  .compliment .band { height: 30px; }
  .compliment .band .black { top: 9px; height: 10px; right: 0; }
  .compliment .band .blue { top: 9px; height: 10px; width: 70px; }
  .compliment .band .badge { right: 28px; top: 0; width: 28px; height: 28px; }
  .compliment .band .badge span { width: 19px; height: 19px; }
</style>
</head>
<body>

<!-- Letterhead -->
<section class="sheet letterhead">
  <div class="wordmark"><span class="name">MARLOW<small>Heating Cooling &amp; Plumbing</small></span><span class="dot"></span></div>
  <div class="contact">
    <div class="line">3167 Penwick Ave</div>
    <div class="line">Findlay, OH 45893</div>
    <div class="line" style="margin-top:5px">(419) 555-0142</div>
    <div class="line">marlowhvacfindlay@examplemail.test</div>
    <div class="line">marlow-hvac.test</div>
  </div>
  <div class="header-rule"></div>
  <div class="letter-body">
    <div class="salutation">Dear Mr. Dalton,</div>
    <p>Lorem ipsum dolor sit amet, consectetuer adipiscing elit, sed diam nonummy nibh euismod tincidunt ut laoreet dolore magna aliquam erat volutpat. Ut wisi enim ad minim veniam, quis nostrud exerci tation ullamcorper suscipit lobortis nisl ut aliquip ex ea commodo consequat. Duis autem vel eum iriure dolor in hendrerit in vulputate velit esse molestie.</p>
    <p>Lorem ipsum dolor sit amet, consectetuer adipiscing elit, sed diam nonummy nibh euismod tincidunt ut laoreet dolore magna aliquam erat volutpat. Ut wisi enim ad minim veniam, quis nostrud exerci tation ullamcorper suscipit lobortis nisl ut aliquip ex ea commodo consequat. Duis autem vel eum iriure dolor in hendrerit in vulputate velit esse molestie.</p>
    <p>Lorem ipsum dolor sit amet, consectetuer adipiscing elit, sed diam nonummy nibh euismod tincidunt ut laoreet dolore magna aliquam erat volutpat. Ut wisi enim ad minim veniam, quis nostrud exerci tation ullamcorper suscipit lobortis nisl ut aliquip ex ea commodo consequat. Duis autem vel eum iriure dolor in hendrerit in vulputate velit esse molestie.</p>
    <p>Lorem ipsum dolor sit amet, consectetuer adipiscing elit, sed diam nonummy nibh euismod tincidunt ut laoreet dolore magna aliquam erat volutpat. Ut wisi enim ad minim veniam, quis nostrud exerci tation ullamcorper suscipit lobortis nisl ut aliquip ex ea commodo consequat. Duis autem vel eum iriure dolor in hendrerit in vulputate velit esse molestie.</p>
    <div class="closing">Regards,</div>
    <div class="signature" role="img" aria-label="Handwritten signature"></div>
  </div>
  <div class="band"><div class="black"></div><div class="blue"></div><div class="badge"><span></span></div></div>
</section>

<!-- Business card front -->
<section class="sheet card-front">
  <div class="wordmark"><span class="name">MARLOW<small>Heating Cooling &amp; Plumbing</small></span><span class="dot"></span></div>
  <div class="divider"></div>
  <div class="contact">
    <div class="line"><svg viewBox="0 0 10 10"><path d="M5 1a3 3 0 0 0-3 3c0 2.2 3 5 3 5s3-2.8 3-5a3 3 0 0 0-3-3z" fill="#1f8fe0"/></svg>3167 Penwick Ave</div>
    <div class="line"><svg viewBox="0 0 10 10"></svg>Findlay, OH 45893</div>
    <div class="line" style="margin-top:4px"><svg viewBox="0 0 10 10"><path d="M2 1h2l1 2.5-1.2.8a5 5 0 0 0 2 2l.8-1.2L9 6v2a1 1 0 0 1-1 1A7 7 0 0 1 1 2a1 1 0 0 1 1-1z" fill="#1f8fe0"/></svg>(419) 555-0142</div>
    <div class="line"><svg viewBox="0 0 10 10"><rect x="1" y="2.5" width="8" height="5" fill="none" stroke="#1f8fe0"/><path d="M1 2.5l4 3 4-3" fill="none" stroke="#1f8fe0"/></svg>marlowhvacfindlay@examplemail.test</div>
    <div class="line"><svg viewBox="0 0 10 10"><circle cx="5" cy="5" r="3.8" fill="none" stroke="#1f8fe0"/><path d="M1.2 5h7.6M5 1.2c2 2.5 2 5.1 0 7.6M5 1.2c-2 2.5-2 5.1 0 7.6" fill="none" stroke="#1f8fe0" stroke-width=".7"/></svg>marlow-hvac.test</div>
  </div>
  <div class="band"><div class="black"></div><div class="blue"></div><div class="badge"><span></span></div></div>
</section>

<!-- Business card back -->
<section class="sheet card-back">
  <div class="wordmark"><span class="name">MARLOW<small>Heating Cooling &amp; Plumbing</small></span><span class="dot"></span></div>
</section>

<!-- Envelope -->
<section class="sheet envelope">
  <svg class="flap" viewBox="0 0 564 227" preserveAspectRatio="none">
    <polyline points="0,0 282,118 564,0" fill="none" stroke="#e6e6e6" stroke-width="1.2"/>
  </svg>
  <div class="wordmark"><span class="name">MARLOW<small>Heating Cooling &amp; Plumbing</small></span><span class="dot"></span></div>
</section>

<!-- Compliment card -->
<section class="sheet compliment">
  <div class="wordmark"><span class="name">MARLOW<small>Heating Cooling &amp; Plumbing</small></span><span class="dot"></span></div>
  <div class="contact">
    <div class="line">3167 Penwick Ave</div>
    <div class="line">Findlay, OH 45893</div>
    <div class="line" style="margin-top:4px">(419) 555-0142</div>
    <div class="line">marlowhvacfindlay@examplemail.test</div>
    <div class="line">marlow-hvac.test</div>
  </div>
  <div class="band"><div class="black"></div><div class="blue"></div><div class="badge"><span></span></div></div>
</section>

</body>
</html>
```